Ferntop Contracting - Civil Construction Construction Company (Telecommunications)

Need a basic website to refine our branding to a current reflection of our service offerings. Ferntop Contracting provides civil construction services specializing in telecommunication sector.
I have started to create a website using word press. I would like to have someone refine the design and polish the overall look and functionality of the site. I would like to website to function in the wordpress format to allow for future edits and control of site.
Included site preview:
https://prv-hosts.pagebuildermock.example/7e2d90aa.com/Admin/index.html/qx_draft_preview
Coding
Coded - Design and coding required
Number of Pages Required
1 page
Look and feel
Each slider illustrates characteristics of the customer's brand and the style your logo design should communicate.

```html
<!DOCTYPE html>
<html lang="en">
<head>
<meta charset="utf-8">
<title>Ferntop Contracting</title>
<link href="https://fonts.googleapis.com/css2?family=Lato:wght@400;700;900&display=swap" rel="stylesheet">
<style>
:root{--red:#ec1c24;--dark:#222;--text:#444;--grey:#efefef;--navy:#1e2636;--white:#fff}
*{box-sizing:border-box;margin:0;padding:0}
html,body{width:1200px;height:4459px;overflow:hidden}
body{font-family:'Lato',sans-serif;color:var(--text);background:var(--white);position:relative}
.wrap{width:1052px;margin:0 auto;position:relative}
.header{height:105px;display:flex;align-items:center;justify-content:space-between;padding:0 75px}
.brand{display:flex;align-items:center;gap:10px;font-size:30px;color:var(--dark);font-weight:400;letter-spacing:1px}
.brand-mark{width:26px;height:26px;background:var(--red)}
.callus{display:flex;align-items:center;gap:16px}
.icon-circle{width:44px;height:44px;border-radius:50%;background:var(--red);display:flex;align-items:center;justify-content:center;flex:none}
.callus small{display:block;color:var(--red);font-size:17px}
.callus strong{font-size:22px;font-weight:400;color:var(--dark)}
.nav{height:70px;background:var(--red)}
.nav ul{list-style:none;display:flex;height:70px;width:1052px;margin:0 auto}
.nav li{color:#fff;font-weight:700;font-size:17px;display:flex;align-items:center;padding:0 34px}
.nav li.active{background:var(--dark)}
.hero{position:relative;height:757px;background:linear-gradient(180deg,#6d7163 0%,#8a8a55 30%,#7a7a3e 60%,#6d6a3b 100%);text-align:center;color:#fff;overflow:hidden}
.hero h1{font-weight:900;font-size:80px;line-height:72px;padding-top:198px;text-shadow:0 2px 6px rgba(0,0,0,.5)}
.hero p{font-weight:700;font-size:38px;margin-top:18px;text-shadow:0 2px 6px rgba(0,0,0,.5)}
.btn{display:inline-block;background:var(--red);color:#fff;font-weight:700;font-size:18px;border-radius:28px;padding:16px 42px}
.hero .btn{margin-top:26px}
.dots{position:absolute;top:610px;left:50%;transform:translateX(-50%);display:flex;gap:10px}
.dots span{width:11px;height:11px;background:#fff}.dots span:first-child{background:#333}
.slant{position:absolute;left:0;width:1200px}
.about{height:606px;position:relative}
.about-text{position:absolute;left:75px;top:70px;width:510px}
.about h2{font-size:42px;font-weight:700;color:var(--red);line-height:48px}
.about h3{font-size:42px;font-weight:700;color:var(--dark);line-height:48px}
.about p{font-size:18px;line-height:30.5px;margin:14px 0 30px}
.about-photo{position:absolute;left:615px;top:73px;width:512px;height:400px;border-radius:26px;background:linear-gradient(135deg,#5c7a3a,#8a8a44 55%,#c9a72a);}
.why{position:relative;height:748px;background:linear-gradient(180deg,#2b3447,#3a4036 60%,#222835)}
.why h2{text-align:center;color:#fff;font-size:42px;font-weight:700;padding-top:140px}
.cards{position:absolute;left:75px;top:235px;display:flex;gap:30px}
.card{width:331px;height:330px;background:#fff;border-radius:6px;padding:28px 24px}
.card ul{list-style:none;margin-top:26px}
.card li{position:relative;padding-left:40px;font-size:18px;line-height:25px;color:var(--text);margin-bottom:15px}
.card li::before{content:"»";position:absolute;left:4px;color:var(--red);font-weight:900;font-size:22px;line-height:22px}
.work{text-align:center;height:927px;position:relative}
.title{font-size:42px;font-weight:700;color:var(--dark)}
.title span{color:var(--red)}
.work .title{padding-top:52px}
.work p.lead{font-size:18px;line-height:30px;margin:18px auto 0;width:1052px}
.grid{display:grid;grid-template-columns:repeat(3,331px);gap:30px;width:1052px;margin:34px auto 0;row-gap:30px}
.grid div{height:259px}
.work .btn{margin-top:64px;padding:16px 56px}
.contact{position:relative;height:1030px;background:var(--grey);text-align:center}
.contact .title{padding-top:150px}
.contact p.lead{font-size:18px;line-height:30px;margin-top:20px}
.info{display:flex;gap:0;position:absolute;left:118px;top:318px;text-align:left}
.info-item{display:flex;gap:20px;width:330px}
.info-item .icon-circle{width:62px;height:62px}
.info-item b{color:var(--red);font-size:18px;font-weight:700;display:block;margin-bottom:4px}
.info-item span{font-size:16px;line-height:26px;color:var(--dark)}
.map{position:absolute;left:75px;top:450px;width:1052px;height:424px;border:3px solid #c8c8c8;background:linear-gradient(135deg,#e5ecdf,#dfe7ea 60%,#e9eee4)}
.footer{text-align:center;padding-top:66px}
.footer ul{list-style:none;display:flex;justify-content:center;gap:56px;font-weight:700;font-size:17px;color:var(--dark)}
.footer small{display:block;font-size:15px;margin-top:24px;color:var(--dark)}
.social{display:flex;justify-content:center;gap:22px;margin-top:18px}
.social span{width:22px;height:22px;border-radius:50%;background:#555}
</style>
</head>
<body>
<header class="header">
  <div class="brand"><span class="brand-mark"></span>FTR CONTRACTING</div>
  <div class="callus">
    <div class="icon-circle"><svg width="22" height="22" viewBox="0 0 24 24"><path fill="#fff" d="M6.6 10.8a15 15 0 0 0 6.6 6.6l2.2-2.2c.3-.3.7-.4 1-.2 1.1.4 2.3.6 3.6.6.6 0 1 .4 1 1V20c0 .6-.4 1-1 1A17 17 0 0 1 3 4c0-.6.4-1 1-1h3.5c.6 0 1 .4 1 1 0 1.3.2 2.5.6 3.6.1.3 0 .7-.2 1z"/></svg></div>
    <div><small>Call Us</small><strong>1 (555) 014-2287</strong></div>
  </div>
</header>
<nav class="nav"><ul><li class="active">HOME</li><li>COMPANY PROFILE</li><li>OUR SERVICES</li><li>WHY CHOOSE US</li><li>OUR WORK</li><li>CONTACT</li></ul></nav>

<section class="hero" role="img" aria-label="Tracked trenching machine laying red conduit in a grassy field with a worker in safety vest">
  <h1>WELCOME TO<br>FERNTOP CONTRACTING</h1>
  <p>We are a Civil Construction Construction Company</p>
  <span class="btn">Contact Us</span>
  <div class="dots"><span></span><span></span><span></span><span></span></div>
  <svg class="slant" style="bottom:0" height="75" viewBox="0 0 1200 75" preserveAspectRatio="none"><polygon points="0,75 1200,75 1200,0 640,75" fill="#fff"/><polygon points="640,75 1200,0 1200,50" fill="#ec1c24"/></svg>
</section>

<section class="about">
  <div class="about-text">
    <h2>About</h2><h3>Company Profile</h3>
    <p>Ferntop Contracting is a safety conscious, productive and efficient construction firm capable of all facets of civil construction. We have completed thousands of projects across Alberta, Saskatchewan and British Columbia working within various industry sectors. We have built a diverse team of skilled professionals who take a great deal of pride in their work and aim to achieve the highest levels of customer satisfaction.</p>
    <span class="btn">Read More</span>
  </div>
  <svg class="slant" style="left:653px;top:465px;width:474px" height="42" viewBox="0 0 474 42"><polygon points="0,10 474,0 474,10 0,42" fill="#ec1c24"/></svg>
  <div class="about-photo" role="img" aria-label="Worker operating a yellow trenching machine on green lawn"></div>
</section>

<section class="why" role="img" aria-label="Dim background of construction equipment at a forest edge" >
  <svg class="slant" style="top:0" height="100" viewBox="0 0 1200 100" preserveAspectRatio="none"><polygon points="0,0 1200,0 1200,0 0,100" fill="#fff"/><polygon points="0,0 0,100 520,100" fill="#ec1c24" opacity="0"/><polygon points="0,0 560,100 0,100" fill="#ec1c24"/></svg>
  <h2>Why Choose Us</h2>
  <div class="cards">
    <div class="card">
      <svg width="64" height="66" viewBox="0 0 64 66"><path d="M32 3 8 12v20c0 16 11 27 24 31 13-4 24-15 24-31V12z" fill="none" stroke="#ec1c24" stroke-width="3"/><path d="M20 33l9 9 16-18" fill="none" stroke="#ec1c24" stroke-width="4"/></svg>
      <ul><li>Accredited health and safety program</li><li>Proven track record of safety excellence</li><li>Continuous training &amp; development of employees</li></ul>
    </div>
    <div class="card">
      <svg width="70" height="66" viewBox="0 0 70 66"><circle cx="30" cy="20" r="10" fill="none" stroke="#ec1c24" stroke-width="3"/><circle cx="30" cy="20" r="4" fill="#ec1c24"/><circle cx="54" cy="12" r="5" fill="none" stroke="#ec1c24" stroke-width="2"/><path d="M4 50h14l12 6h18l14-12" fill="none" stroke="#ec1c24" stroke-width="3"/></svg>
      <ul><li>Productive and efficient crews</li><li>Current fleet of modern equipment</li><li>Use of latest construction techniques/technologies</li></ul>
    </div>
    <div class="card">
      <svg width="70" height="66" viewBox="0 0 70 66"><path d="M4 20l14-10 14 8 14-8 20 12-10 16-20 16-22-14z" fill="none" stroke="#ec1c24" stroke-width="3"/><path d="M24 30l10 8M30 26l12 10" stroke="#ec1c24" stroke-width="3"/></svg>
      <ul><li>Quality and process driven</li><li>Excellent customer service</li><li>Privately owned &amp; operated</li><li>Dependable, Reliable &amp; Honest</li></ul>
    </div>
  </div>
  <svg class="slant" style="bottom:0" height="100" viewBox="0 0 1200 100" preserveAspectRatio="none"><polygon points="0,100 1200,0 1200,100" fill="#fff"/><polygon points="600,50 1200,0 1200,100" fill="#ec1c24"/></svg>
</section>

<section class="work">
  <h2 class="title"><span>Our</span> Work</h2>
  <p class="lead">Ferntop Contracting is equipped to complete civil construction projects of all sizes and complexities. From small alterations and repairs to large scale network deployments throughout large geographical areas.</p>
  <div class="grid">
    <div role="img" aria-label="Close-up of blue drilling equipment with gauges" style="background:linear-gradient(135deg,#4a9ab8,#8a8f90)"></div>
    <div role="img" aria-label="Tracked utility vehicle carrying red conduit reel" style="background:linear-gradient(135deg,#7aa0c4,#8a3a30 60%,#333)"></div>
    <div role="img" aria-label="Yellow dozer with red cable reel by autumn trees" style="background:linear-gradient(135deg,#b8a23a,#6f7d3a 60%,#b33a2a)"></div>
    <div role="img" aria-label="Directional drilling rig at a residential site" style="background:linear-gradient(135deg,#9ab2c6,#5a6a4a 50%,#222)"></div>
    <div role="img" aria-label="Operator seated at drilling machine controls" style="background:linear-gradient(135deg,#9fb4c8,#4a5a44 50%,#2a2a2a)"></div>
    <div role="img" aria-label="Red trenching machine working along a treeline" style="background:linear-gradient(135deg,#6a7a4a,#8a3a2a 50%,#3a2a22)"></div>
  </div>
  <span class="btn">View All</span>
</section>

<section class="contact">
  <svg class="slant" style="top:0" height="100" viewBox="0 0 1200 100" preserveAspectRatio="none"><polygon points="0,0 0,100 600,50" fill="#ec1c24"/><polygon points="0,0 1200,0 1200,100 600,50" fill="#fff"/><polygon points="0,0 600,50 1200,0" fill="#fff"/></svg>
  <h2 class="title"><span>Our</span> Contact Location</h2>
  <p class="lead">If you would like to know more about our services please call or provide the information below.<br>Thank you for your interest in Ferntop Contracting</p>
  <div class="info">
    <div class="info-item"><div class="icon-circle"><svg width="22" height="28" viewBox="0 0 22 28"><path d="M11 0a11 11 0 0 0-11 11c0 8 11 17 11 17s11-9 11-17A11 11 0 0 0 11 0z" fill="#fff"/><circle cx="11" cy="11" r="4" fill="#ec1c24"/></svg></div><div><b>Address:</b><span>18 Quarry Lane<br>Birchfield, AB T9Z 4K2<br>Canada</span></div></div>
    <div class="info-item"><div class="icon-circle"><svg width="24" height="24" viewBox="0 0 24 24"><path fill="#fff" d="M6.6 10.8a15 15 0 0 0 6.6 6.6l2.2-2.2c.3-.3.7-.4 1-.2 1.1.4 2.3.6 3.6.6.6 0 1 .4 1 1V20c0 .6-.4 1-1 1A17 17 0 0 1 3 4c0-.6.4-1 1-1h3.5c.6 0 1 .4 1 1 0 1.3.2 2.5.6 3.6.1.3 0 .7-.2 1z"/></svg></div><div><b>Phone No</b><span style="font-weight:700">1 (555) 014-2287</span></div></div>
    <div class="info-item"><div class="icon-circle"><svg width="26" height="20" viewBox="0 0 26 20"><rect width="26" height="20" rx="2" fill="#fff"/><path d="M1 2l12 9 12-9" fill="none" stroke="#ec1c24" stroke-width="2"/></svg></div><div><b>Email</b><span style="font-weight:700">info@ferntopcontracting.example</span></div></div>
  </div>
  <div class="map" role="img" aria-label="Street map showing the office location"></div>
  <svg class="slant" style="bottom:0" height="100" viewBox="0 0 1200 100" preserveAspectRatio="none"><polygon points="0,100 1200,100 1200,0" fill="#fff"/><polygon points="620,30 1200,0 1200,100" fill="#ec1c24"/></svg>
</section>

<footer class="footer">
  <ul><li>HOME</li><li>COMPANY PROFILE</li><li>OUR SERVICES</li><li>WHY CHOOSE US</li><li>OUR WORK</li><li>CONTACT</li></ul>
  <small>Copyright © 2022, Company Name All Right reserved</small>
  <div class="social" aria-label="Social links"><span></span><span></span><span></span><span></span><span></span></div>
</footer>
</body>
</html>
```